UI/UX Re-Do for TallyNest - a free to use project management platform for desktop and mobile.

UI/UX Re-Do for TallyNest
TallyNest is a free to use project management platform for desktop and mobile.
We are looking for help with our UI/UX re-design.
As of now the platform is totally functional.
The problem is around flow and look. We want TN to become something that any one can use to manage and even socialize any project. A project can be something work related like organizing a team around a software build, marketing campaign, shared client file space, etc... In fact, most of our current members are using TN for just such work projects.
We also see a project as planning a wedding, organizing a group trip, a simple to-do list, organizing a kids sports team, and so on...
To become a platform that people will use in their work and personal life we first need to become more intuitive and friendly - while maintaining advanced functionality for more advanced needs.
We need help to beautify, streamline, and simplify - while keeping all the functions.
The quickest way to understand TN, and our current issues is this short video:
https://vidhost.example/Qw8ZmT3pLsK
For sure see this link for the entire most recent description AND images:
https://tallynestapp.example/?p=KumrT4WdZeL
The best way to understand TN is to actually use it:
https://tallynestapp.example
Should you choose to take a run at improving TN here are the details:
Please focus your ideas for mobile, it's where we have the biggest issues.
Feel free to get outside the box.
Avoid swipe oriented designs.
Feel free to focus on ideas over polished outputs.
Use any tool you like, PS, hand drawing, written description if you think that works best.
(FYI - we use mostly use Vellum Slides docs internally)
Point is illustration of ideas over tool choice.
Feel free to:
Create something totally new
And/or riff on what we have now
And/or riff on the new design we are considering (see images below)
|||
If we go the direction of the images/designs below the idea is to give people options on how they see/experience TN.
Just below is what we are calling Base Mode. This is a more basic and simple flow. Probably a default to keep new users feeling comfortable at the start.
<img src="https://picbin.example/8hTzqWL.jpg" style="width: 100%;">
https://picbin.example/8hTzqWL.jpg
|||
We are calling this optional view Peak Mode. It is more advanced and can show all project, goal(renamed 'milestones') at the same time. This is more of a paint job on the current design.
<img src="https://picbin.example/vNmd2Rs.jpg" style="width: 100%;">
https://picbin.example/vNmd2Rs.jpg
|||
If you're submitting please let us know if you can also do the PS files for dev.
Not required, but once we nail down the concepts we want someone to hone in the PS files.
As an optional bonus we will also be giving credit to you/your company in TN.
Let us know if you do or don't want that.
We are excited to see your work!!
Target Market(s)
Anyone who needs to organize any project, big or small. The key is to make a super friendly user experience for new users while retaining advanced functions.
Industry/Entity Type
Management
Number of Pages Required
2 page
Look and feel

```html
<!DOCTYPE html>
<html lang="en">
<head>
<meta charset="utf-8">
<title>TallyNest – My Projects</title>
<link href="https://fonts.googleapis.com/css2?family=Poppins:wght@300;400;500;600&family=Roboto:wght@500&display=swap" rel="stylesheet">
<style>
  :root {
    --brand-red: #ef5a5f;
    --brand-red-soft: #f49294;
    --topbar-blue: #4a88f7;
    --accent-blue: #4a88f7;
    --page-bg: #f4f5f8;
    --panel-bg: #ffffff;
    --line: #e6e8ec;
    --text-dark: #464b55;
    --text-mid: #5d626c;
    --text-muted: #8f939c;
    --icon-grey: #9a9ea7;
    --badge-dark: #1b1b1b;
  }
  * { box-sizing: border-box; margin: 0; padding: 0; }
  html, body { width: 1200px; height: 752px; overflow: hidden; }
  body {
    font-family: "Poppins", sans-serif;
    background: var(--page-bg);
    color: var(--text-dark);
    position: relative;
  }

  /* Sidebar */
  .sidebar {
    position: absolute; left: 0; top: 0;
    width: 234px; height: 752px;
    background: var(--panel-bg);
  }
  .brand {
    position: absolute; left: 30px; top: 20px;
    font-size: 19px; font-weight: 600; color: var(--brand-red-soft);
    letter-spacing: 0.3px;
  }
  .menu-toggle { position: absolute; left: 197px; top: 24px; }
  .avatar {
    position: absolute; left: 62px; top: 80px;
    width: 108px; height: 108px; border-radius: 50%;
    background: linear-gradient(90deg, #d9d6d3 0%, #b9b3ad 45%, #f2b84b 75%, #f6c35a 100%);
  }
  .user-name {
    position: absolute; left: 0; top: 198px; width: 234px;
    text-align: center; font-size: 20px; font-weight: 400; color: var(--text-mid);
  }
  .nav { position: absolute; left: 0; top: 294px; width: 234px; list-style: none; }
  .nav-item {
    position: relative; height: 45px;
    display: flex; align-items: center;
    padding-left: 30px; font-size: 13px; color: var(--text-muted);
  }
  .nav-item svg { width: 17px; height: 17px; margin-right: 16px; fill: var(--icon-grey); }
  .nav-item.is-active { color: var(--text-dark); font-weight: 500; }
  .nav-item.is-active::before {
    content: ""; position: absolute; left: 0; top: 8px;
    width: 4px; height: 32px; background: var(--brand-red);
  }
  .nav-item .caret { position: absolute; left: 203px; top: 17px; width: 12px; height: 12px; margin: 0; }
  .copyright {
    position: absolute; left: 0; top: 712px; width: 234px;
    text-align: center; font-size: 12.5px; color: var(--text-mid);
  }

  /* Top bar */
  .topbar {
    position: absolute; left: 234px; top: 0;
    width: 966px; height: 60px; background: var(--topbar-blue);
  }
  .search { position: absolute; left: 44px; top: 19px; display: flex; align-items: center; }
  .search-label {
    margin-left: 12px; font-family: "Roboto", sans-serif;
    font-size: 11.5px; font-weight: 500; color: #ffffff;
  }
  .view-switch {
    position: absolute; left: 830px; top: 0; height: 60px; width: 136px;
    border-left: 1px solid rgba(255,255,255,0.15);
  }
  .view-base { position: absolute; left: 24px; top: 23px; }
  .view-peak { position: absolute; left: 62px; top: 17px; }

  /* Panels */
  .panel { position: absolute; background: var(--panel-bg); box-shadow: 0 1px 2px rgba(0,0,0,0.04); }
  .picks { left: 278px; top: 105px; width: 341px; height: 505px; }
  .picks-head {
    height: 56px; border-bottom: 1px solid var(--line);
    display: flex; align-items: center; justify-content: space-between;
    padding: 0 16px 0 18px; font-size: 14.5px; color: var(--brand-red);
  }
  .pick-list { list-style: none; padding: 44px 18px 0; }
  .pick-card {
    height: 48px; border: 1px solid var(--line); margin-bottom: 10px;
    position: relative; padding: 9px 0 0 13px;
  }
  .pick-title { font-size: 13px; color: var(--text-mid); line-height: 1.2; }
  .pick-status { font-size: 9px; color: var(--text-muted); margin-top: 2px; }
  .pick-card .go { position: absolute; right: 29px; top: 19px; }
  .pick-card .more { position: absolute; right: 15px; top: 18px; }
  .link-list { list-style: none; margin-top: 30px; }
  .link-row {
    height: 52px; display: flex; align-items: center; justify-content: space-between;
    padding: 0 18px; font-size: 15px; color: var(--text-mid);
  }
  .link-row + .link-row { border-top: 1px solid var(--line); }

  .welcome { left: 664px; top: 105px; width: 492px; height: 506px; padding: 98px 63px 0 44px; }
  .welcome-kicker { font-size: 18px; font-weight: 300; color: var(--accent-blue); }
  .welcome-title { font-size: 31px; font-weight: 600; color: var(--text-dark); margin-top: 2px; letter-spacing: 0.2px; }
  .welcome-text {
    font-size: 14px; line-height: 25px; color: var(--text-mid);
    text-align: justify; margin-top: 14px;
  }
  .welcome-text + .welcome-text { margin-top: 22px; }
  .store-badges { display: flex; gap: 8px; margin-top: 22px; }
  .store-badge { width: 118px; height: 42px; border-radius: 4px; background: var(--badge-dark); }
</style>
</head>
<body>
  <aside class="sidebar">
    <div class="brand">TallyNest</div>
    <svg class="menu-toggle" width="20" height="16" viewBox="0 0 20 16"><g stroke="#444" stroke-width="1.8"><line x1="0" y1="1" x2="20" y2="1"/><line x1="0" y1="8" x2="20" y2="8"/><line x1="0" y1="15" x2="20" y2="15"/></g></svg>
    <div class="avatar" role="img" aria-label="Profile photo of the signed-in user"></div>
    <div class="user-name">Marisol Vega</div>
    <ul class="nav">
      <li class="nav-item is-active">
        <svg viewBox="0 0 16 16"><rect x="1" y="2" width="14" height="9" rx="1" fill="none" stroke="#9a9ea7" stroke-width="1.4"/><rect x="4" y="6" width="2" height="4"/><rect x="7" y="4" width="2" height="6"/><rect x="10" y="7" width="2" height="3"/><path d="M8 11 L5 15 M8 11 L11 15" stroke="#9a9ea7" stroke-width="1.2"/></svg>
        My Projects
        <svg class="caret" viewBox="0 0 12 12"><path d="M2 4 L6 8 L10 4" fill="none" stroke="#ef5a5f" stroke-width="1.8"/></svg>
      </li>
      <li class="nav-item">
        <svg viewBox="0 0 20 16"><circle cx="10" cy="4" r="3"/><circle cx="4" cy="6" r="2.3"/><circle cx="16" cy="6" r="2.3"/><path d="M4 15 a6 6 0 0 1 12 0z"/><path d="M0 14 a4 4 0 0 1 5 -4 l-1 4z M20 14 a4 4 0 0 0 -5 -4 l1 4z"/></svg>
        Public Projects
      </li>
      <li class="nav-item">
        <svg viewBox="0 0 16 16"><path d="M7 0h2l.4 2.2 1.5.6 1.8-1.3 1.4 1.4-1.3 1.8.6 1.5 2.2.4v2l-2.2.4-.6 1.5 1.3 1.8-1.4 1.4-1.8-1.3-1.5.6L9 16H7l-.4-2.2-1.5-.6-1.8 1.3-1.4-1.4 1.3-1.8-.6-1.5L0 9V7l2.2-.4.6-1.5L1.5 3.3l1.4-1.4 1.8 1.3 1.5-.6z"/><circle cx="8" cy="8" r="2.6" fill="#fff"/></svg>
        Admin
      </li>
      <li class="nav-item">
        <svg viewBox="0 0 16 16"><path d="M1 2h6v2H3v8h4v2H1z"/><path d="M6 6.5h5V3.5l5 4.5-5 4.5v-3H6z"/></svg>
        Sign Out
      </li>
      <li class="nav-item">
        <svg viewBox="0 0 16 16"><circle cx="8" cy="8" r="7"/><rect x="7" y="7" width="2" height="5" fill="#fff"/><circle cx="8" cy="4.8" r="1.1" fill="#fff"/></svg>
        About TallyNest
      </li>
      <li class="nav-item">
        <svg viewBox="0 0 16 16"><path d="M3 1h7l4 4v10H3z" fill="none" stroke="#9a9ea7" stroke-width="1.4"/><g stroke="#9a9ea7" stroke-width="1.2"><line x1="5.5" y1="8" x2="11.5" y2="8"/><line x1="5.5" y1="10.5" x2="11.5" y2="10.5"/><line x1="5.5" y1="13" x2="11.5" y2="13"/></g></svg>
        Terms and Condition
      </li>
    </ul>
    <div class="copyright">© 2017 All Rights Reserved</div>
  </aside>

  <header class="topbar">
    <div class="search">
      <svg width="21" height="21" viewBox="0 0 21 21"><circle cx="8.5" cy="8.5" r="7" fill="none" stroke="#fff" stroke-width="1.8"/><line x1="13.6" y1="13.6" x2="20" y2="20" stroke="#fff" stroke-width="2"/></svg>
      <span class="search-label">Search revenue here...</span>
    </div>
    <div class="view-switch">
      <svg class="view-base" width="26" height="15" viewBox="0 0 26 15"><rect x="0" y="0" width="3" height="15" fill="#7aa8fa"/><rect x="5" y="0" width="21" height="15" fill="#7aa8fa"/></svg>
      <svg class="view-peak" width="30" height="27" viewBox="0 0 30 27"><rect width="30" height="27" fill="#fff"/><rect x="6" y="5" width="4" height="17" fill="#4a88f7"/><rect x="13" y="5" width="4" height="17" fill="#4a88f7"/><rect x="20" y="5" width="4" height="17" fill="#4a88f7"/></svg>
    </div>
  </header>

  <section class="panel picks">
    <div class="picks-head">
      <span>TallyNest Top Projects Picks</span>
      <svg width="14" height="10" viewBox="0 0 14 10"><path d="M1.5 2 L7 7.5 L12.5 2" fill="none" stroke="#ef5a5f" stroke-width="2"/></svg>
    </div>
    <ul class="pick-list">
      <li class="pick-card">
        <div class="pick-title">Startup starter Kit</div>
        <div class="pick-status">Status</div>
        <svg class="go" width="6" height="9" viewBox="0 0 6 9"><path d="M1 1 L5 4.5 L1 8" fill="none" stroke="#777" stroke-width="1.3"/></svg>
        <svg class="more" width="3" height="12" viewBox="0 0 3 12"><g fill="#d0d2d6"><circle cx="1.5" cy="1.5" r="1.3"/><circle cx="1.5" cy="6" r="1.3"/><circle cx="1.5" cy="10.5" r="1.3"/></g></svg>
      </li>
      <li class="pick-card">
        <div class="pick-title">TN Public Project Info</div>
        <div class="pick-status">Status</div>
        <svg class="go" width="6" height="9" viewBox="0 0 6 9"><path d="M1 1 L5 4.5 L1 8" fill="none" stroke="#777" stroke-width="1.3"/></svg>
        <svg class="more" width="3" height="12" viewBox="0 0 3 12"><g fill="#d0d2d6"><circle cx="1.5" cy="1.5" r="1.3"/><circle cx="1.5" cy="6" r="1.3"/><circle cx="1.5" cy="10.5" r="1.3"/></g></svg>
      </li>
    </ul>
    <ul class="link-list">
      <li class="link-row">Most Popular Public Projects
        <svg width="8" height="13" viewBox="0 0 8 13"><path d="M1.5 1.5 L6.5 6.5 L1.5 11.5" fill="none" stroke="#8f939c" stroke-width="1.8"/></svg>
      </li>
      <li class="link-row">All Public Projects
        <svg width="8" height="13" viewBox="0 0 8 13"><path d="M1.5 1.5 L6.5 6.5 L1.5 11.5" fill="none" stroke="#8f939c" stroke-width="1.8"/></svg>
      </li>
    </ul>
  </section>

  <section class="panel welcome">
    <p class="welcome-kicker">Welcome To</p>
    <h1 class="welcome-title">Your My Project' Area!</h1>
    <p class="welcome-text">You are currently active on your 'My Projects' Umbrella. From here you can manage existing projects and create new projects and umbrellas.</p>
    <p class="welcome-text">To create a new project look just below the ' My Projects' umbrella and click the 'Create Project' button.</p>
    <div class="store-badges">
      <div class="store-badge" role="img" aria-label="Mobile app store download badge"></div>
      <div class="store-badge" role="img" aria-label="Mobile app store download badge"></div>
    </div>
  </section>
</body>
</html>
```